E-Commerce startup needs a Brellix store front

Tallow are looking for help designing and building a Brellix store front.

So what do we need?

A simple, user-friendly home page to display menu options and collections of products.

It’s got to be clean. Uncluttered.

No screaming starbursts! No sale countdown timers.

Clean.

Functional. Clean.

Looks great in mobile. Clean.

Clean but not cold. Needs personality. Design should cue trust and quality.

How it will work is this: every update cycle, we’ll add 5 new products to the site. 5 umbrellas, 5 travel mugs, 5 candle holders, etc. We will need a key frame that will hold an image and a headline. We want these frames to feel consistent from one product to the next. It’s important to note that the headlines are key to personality of the site and their treatment should not be overlooked.

Consistent headline style
Consistent background type (solo product or product in-situ)
Consistent branding cues

While these product frames will be the meat of the site, there are other considerations, as well.

When we click on a product key frame, it will take us to a page with that product collection. There will be the 5 products with supporting copy (product details/specs) and images for each. What should this page look like?

What should the header/navigation look like?

What about the footer?

How about the feature image on home/landing page?

How should we handle copy heavy pages (About us, Shipping policy, returns, etc)

Guidelines:
Colour palette to be based on logo but can expand from there.
San-serif fonts
Needs to work across popular devices (mobile/desktop/tablet) and operating systems. With flexibility to expand into an app in the future.

Some multi-category sites we like:

Quorvane.com – Clean header, design and colours feel warm, friendly
Delphwick.com – The rounded feature boxes are cheerful, inviting
Pell.co.uk – Large images, nice photography, stylish consistent

Some sites we don’t love the look of

Rimu.co.uk – Products photos are too inconsistent in size, shape and style. Looks messy.
Zoba.com – Too many sale offers, pop ups, deals, deals, deals. Feels cheap and desperate.
Frandle.co.uk – Feels like an overwhelming amount of information and boxes.

Please feel free to contact us with questions.

Thank you for your designs and expertise. Looking forward to seeing your work.

```html
<!DOCTYPE html>
<html lang="en">
<head>
<meta charset="utf-8">
<title>Tallow – Home</title>
<link rel="stylesheet" href="https://fonts.googleapis.com/css2?family=Montserrat:wght@400;500;600;700;800&family=Righteous&family=Tinos&display=swap">
<style>
:root{
  --red:#e83a36;
  --red-dark:#d22e2a;
  --blush:#fdf0f0;
  --card-pink:#fdeeee;
  --gold:#e2a417;
  --ink:#111111;
  --white:#ffffff;
  --ghost:#ececec;
}
*{margin:0;padding:0;box-sizing:border-box}
html,body{width:1200px;height:2166px;overflow:hidden;background:var(--white)}
body{position:relative;font-family:"Montserrat",sans-serif;color:var(--ink)}
a{color:inherit;text-decoration:none}

/* header */
.site-header{position:absolute;left:0;top:0;width:1200px;height:85px;background:var(--blush)}
.brand{position:absolute;left:115px;top:12px;font-weight:800;font-size:58px;line-height:60px;color:var(--red);letter-spacing:1px}
.search{position:absolute;left:381px;top:22px;width:456px;height:40px;border:2px solid var(--red);border-radius:20px;background:var(--white)}
.search span{position:absolute;left:15px;top:10px;font-size:12px;color:#333}
.search svg{position:absolute;right:16px;top:8px}
.account{position:absolute;left:877px;top:35px;font-size:12.5px;color:#222}
.account-icon{position:absolute;left:1026px;top:32px}
.cart-icon{position:absolute;left:1067px;top:32px}

.main-nav{position:absolute;left:0;top:85px;width:1200px;height:45px;background:var(--red)}
.main-nav a{position:absolute;top:16px;font-size:12px;color:var(--white);font-weight:500}

/* hero */
.hero{position:absolute;left:0;top:130px;width:1200px;height:557px;
  background:linear-gradient(180deg,#e4e4e0 0%,#d7d9d2 35%,#b9b59e 62%,#c7a584 85%,#a9825c 100%)}
.hero-panel{position:absolute;left:261px;top:85px;width:678px;height:256px;background:rgba(232,58,54,.72);border-radius:6px;text-align:center}
.hero-panel h1{font-family:"Righteous",sans-serif;font-weight:400;color:var(--white);font-size:40px;line-height:47px;margin-top:44px;letter-spacing:.3px}
.btn{display:block;position:absolute;color:var(--white);font-weight:600;font-size:16px;text-align:center;border-radius:4px}
.btn-gold{left:271px;top:158px;width:137px;height:47px;line-height:47px;background:var(--gold)}
.scroll-cue{position:absolute;left:537px;top:627px;width:120px;height:120px;border-radius:50%;background:var(--white)}
.scroll-cue svg{position:absolute;left:37px;top:30px}

/* collections */
.section-title{position:absolute;left:0;top:744px;width:1200px;text-align:center;font-family:"Righteous",sans-serif}
.section-title .ghost{display:block;font-size:80px;line-height:84px;color:var(--ghost)}
.section-title h2{position:absolute;left:0;top:20px;width:1200px;font-weight:400;font-size:45px;line-height:52px;color:var(--ink)}

.card{position:absolute;width:312px;height:301px;background:var(--card-pink);border-radius:8px;box-shadow:0 2px 8px rgba(0,0,0,.08)}
.card .photo{position:absolute;left:40px;top:30px;width:232px;height:210px;border-radius:6px}
.card .photo.bleed{left:0;top:0;width:298px;height:290px;border-radius:8px}
.card-info{position:absolute;width:279px;height:155px;background:var(--white);border-radius:10px;box-shadow:0 2px 10px rgba(0,0,0,.1);text-align:center;font-size:17px;font-weight:500;line-height:29px}
.card-info p{padding-top:14px}
.card-info .price{position:absolute;left:0;width:100%;bottom:14px;font-size:18px;font-weight:400;padding:0}

.btn-red{left:531px;top:1738px;width:137px;height:47px;line-height:47px;background:var(--red)}

/* footer */
.site-footer{position:absolute;left:0;top:1845px;width:1200px;height:274px;background:var(--red);color:var(--white)}
.footer-brand{position:absolute;left:115px;top:76px;font-weight:800;font-size:56px;color:var(--white)}
.footer-col{position:absolute;top:89px}
.footer-col h3{font-size:22px;font-weight:600;line-height:26px;margin-bottom:20px}
.footer-col li{list-style:none;font-size:14.5px;line-height:28.5px;padding-left:3px}
.social{display:flex;flex-direction:column;gap:8px;margin-top:2px}
.social a{display:flex;align-items:center;gap:10px;font-size:14.5px}
.social i{display:block;width:26px;height:26px;border:1.6px solid var(--white);border-radius:50%}
.legal{position:absolute;left:0;top:2119px;width:1200px;height:47px;background:var(--red-dark);color:var(--white);font-family:"Tinos",serif;font-size:13.5px;text-align:center;line-height:40px}
</style>
</head>
<body>

<header class="site-header">
  <div class="brand">Tallow</div>
  <div class="search">
    <span>What Are You looking For?</span>
    <svg width="22" height="22" viewBox="0 0 22 22" fill="none" stroke="#111" stroke-width="2"><circle cx="9" cy="9" r="7"/><line x1="14" y1="14" x2="20" y2="20"/></svg>
  </div>
  <div class="account">SIGN IN/ MY ACCOUNT</div>
  <svg class="account-icon" width="18" height="18" viewBox="0 0 18 18" fill="#111"><circle cx="9" cy="5" r="4"/><path d="M1 18c0-5 3.5-7.5 8-7.5s8 2.5 8 7.5z"/></svg>
  <svg class="cart-icon" width="18" height="18" viewBox="0 0 18 18" fill="#111"><path d="M2 4h14l-1 13H3z"/><path d="M6 7a3 3 0 0 0 6 0" stroke="#fff" stroke-width="1.5" fill="none"/></svg>
</header>

<nav class="main-nav">
  <a style="left:166px">HOME &amp; GARDEN</a>
  <a style="left:324px">SPORT &amp; FITNESS</a>
  <a style="left:481px">PETS</a>
  <a style="left:562px">KIDS</a>
  <a style="left:642px">BABIES</a>
  <a style="left:738px">MEN</a>
  <a style="left:818px">WOMEN</a>
  <a style="left:920px">GIFTS</a>
  <a style="left:1002px">NEW</a>
</nav>

<section class="hero" role="img" aria-label="Potted houseplants on a wooden shelf against a pale wall">
  <div class="hero-panel">
    <h1>5 Fake Houseplants For The<br>Criminally Negligent</h1>
    <a class="btn btn-gold">Show Me</a>
  </div>
</section>
<div class="scroll-cue">
  <svg width="46" height="58" viewBox="0 0 46 58" fill="none" stroke="#111" stroke-width="3.5"><rect x="2" y="2" width="42" height="54" rx="21"/><line x1="23" y1="10" x2="23" y2="20"/></svg>
</div>

<div class="section-title">
  <span class="ghost">Recent Additions</span>
  <h2>Recent Additions</h2>
</div>

<article class="card" style="left:105px;top:860px">
  <div class="photo" role="img" aria-label="Black portable power bank" style="background:linear-gradient(180deg,#3a3a3a,#141414)"></div>
</article>
<div class="card-info" style="left:122px;top:1114px"><p>5 portable chargers<br>FOR when mum needs a<br>quick chat</p><p class="price">$15.99</p></div>

<article class="card" style="left:446px;top:860px">
  <div class="photo" role="img" aria-label="Green pet collar with paw tag" style="background:linear-gradient(180deg,#a5d15a,#82b838)"></div>
</article>
<div class="card-info" style="left:462px;top:1114px"><p>5 brilliant collars<br>FOR budget conscious<br>border collies</p><p class="price">$59.99</p></div>

<article class="card" style="left:779px;top:860px">
  <div class="photo bleed" role="img" aria-label="Wedges of cheese on a wooden board" style="background:linear-gradient(180deg,#f4d752,#d6a45e)"></div>
</article>
<div class="card-info" style="left:795px;top:1114px"><p style="padding-top:30px">5 cheese boards<br>FOR asiago aficionados</p><p class="price">$189.99</p></div>

<article class="card" style="left:105px;top:1297px">
  <div class="photo" role="img" aria-label="Box of colourful baby toys with a teddy bear" style="background:linear-gradient(180deg,#e6bf92,#eceef0)"></div>
</article>
<div class="card-info" style="left:122px;top:1550px"><p>5 sensory toys<br>FOR babies that are<br>easily amazed</p><p class="price">$15.99</p></div>

<article class="card" style="left:446px;top:1297px">
  <div class="photo" role="img" aria-label="Fabric storage bin with a green dinosaur print" style="background:linear-gradient(180deg,#cfe0cc,#6fae78)"></div>
</article>
<div class="card-info" style="left:462px;top:1550px"><p>5 fun storage containers<br>FOR your children to<br>throw</p><p class="price">$59.99</p></div>

<article class="card" style="left:779px;top:1297px">
  <div class="photo" role="img" aria-label="Black and blue gaming chair" style="background:linear-gradient(180deg,#2a4f78,#1c1c1c)"></div>
</article>
<div class="card-info" style="left:795px;top:1550px"><p style="padding-top:17px">5 gaming chairs<br>FOR heroes with<br>princesses to save</p><p class="price">$189.99</p></div>

<a class="btn btn-red">View All</a>

<footer class="site-footer">
  <div class="footer-brand">Tallow</div>
  <div class="footer-col" style="left:416px">
    <h3>Quick Links</h3>
    <ul><li>About Us</li><li>FAQ</li><li>Contact US</li><li>Track My Order</li></ul>
  </div>
  <div class="footer-col" style="left:661px">
    <h3>Other Links</h3>
    <ul><li>Return Policy</li><li>Shipping Policy</li><li>Terms of Service</li></ul>
  </div>
  <div class="footer-col" style="left:919px">
    <h3>Follow Us</h3>
    <div class="social">
      <a><i></i>Flockly</a>
      <a><i></i>Chirra</a>
      <a><i></i>Snapvue</a>
    </div>
  </div>
</footer>
<div class="legal">© 2024 Tallow&nbsp; All rights reserved</div>

</body>
</html>
```